Menu Design Project for new restauranct concept

Design menu for new restaurant concept called Juniper's Burgers & Dogs. Logo is attached.

Industry/Entity Type

Restaurant

Requirements
Must have
• Menu items and pricing:

Burgers
Snack Burger $3.49
Snack Cheeseburger $3.99
Juniper's signature Burger $4.99
Juniper's signature Cheeseburger $5.49
Burger toppings: bacon, lettuce, tomato, onion, pickle, grilled onions, grilled mushrooms, grilled green peppers, jalapeƱo peppers.

Dogs
Hot Dog $2.99
Bacon Cheese Hot Dog $3.99
Slaw Dog $3.99
Kraut Dog $3.49
Chili Dog $3.99 with or with out cheese
Hot dogs are 100% beef

Other
Grilled Chicken Sandwich $5.99
Grilled Chicken Sandwich with cheese $6.49
(Same toppings as burgers)

French Fries $1.99

Loaded Potatos
The Plain Tater: $4.99 choose from: butter, sour cream, cheese, chives
The Garden Tater: $5.99 choose from: the Basic plus, broccoli & cheese, grilled mushrooms, onions, & peppers
The Rancher Tater: $6.99 choose from the Basic/Veggie plus: grilled chicken, chili, Philly cheesesteak, pulled pork.

Drinks
32oz. Drink $1.88
20oz. Drink $1.69

attached logo.
Nice to have
• love to incorporate the woodgrain backgound. It makes the logo look most like a cattle brand, which we like.

```html
<!DOCTYPE html>
<html lang="en">
<head>
<meta charset="utf-8">
<title>Juniper's Burgers &amp; Dogs – Food Menu</title>
<link rel="stylesheet" href="https://fonts.googleapis.com/css2?family=Open+Sans:wght@400;700&display=swap">
<style>
  :root {
    --wood-dark: #2b2521;
    --wood-mid: #3d3530;
    --brand-red: #ed1c24;
    --dogs-red: #be1e2d;
    --logo-ink: #4a1612;
    --label-orange: #f7941d;
    --other-orange: #f15a29;
    --sides-yellow: #fbb040;
    --sides-ink: #3a2414;
    --wine: #a3245a;
    --white: #ffffff;
  }
  * { margin: 0; padding: 0; box-sizing: border-box; }
  html, body { width: 925px; height: 1200px; overflow: hidden; }
  body {
    font-family: "Open Sans", Arial, sans-serif;
    color: var(--white);
    background: var(--wood-dark);
  }
  .menu { position: relative; width: 925px; height: 1200px; overflow: hidden; }

  .woodgrain {
    position: absolute; inset: 0;
    background: linear-gradient(100deg, var(--wood-dark) 0%, var(--wood-mid) 35%, var(--wood-dark) 60%, var(--wood-mid) 100%);
  }
  .swirl-decoration {
    position: absolute; left: 300px; top: 260px; width: 400px; height: 420px;
    border-radius: 50%;
    background: radial-gradient(circle, rgba(247,165,49,0.22) 0%, rgba(247,165,49,0.10) 55%, rgba(247,165,49,0) 72%);
  }
  .top-swirl-decoration {
    position: absolute; left: 520px; top: 0; width: 260px; height: 200px;
    background: radial-gradient(ellipse at 50% 30%, rgba(237,28,36,0.25) 0%, rgba(237,28,36,0) 70%);
  }

  .panel { position: absolute; border-radius: 18px; }
  .panel--brand { left: 34px; top: 34px; width: 318px; height: 644px; background: var(--brand-red); }
  .panel--dogs { left: 34px; top: 706px; width: 318px; height: 284px; background: var(--dogs-red); }
  .panel--other { left: 374px; top: 828px; width: 294px; height: 158px; background: var(--other-orange); }
  .panel--food-menu { position: absolute; left: 644px; top: 198px; width: 281px; height: 432px; background: var(--label-orange); }
  .panel--sides { left: 10px; top: 1026px; width: 900px; height: 164px; background: var(--sides-yellow); color: var(--sides-ink); border-radius: 14px; }

  .brand-mark {
    position: absolute; left: 99px; top: 46px; width: 170px; height: 170px;
    border: 6px solid var(--logo-ink); border-radius: 50%;
  }
  .brand-name {
    position: absolute; left: 0; top: 232px; width: 318px;
    text-align: center; font-weight: 700; font-size: 30px; line-height: 38px;
    color: var(--logo-ink);
  }

  .section-label {
    position: absolute; background: var(--label-orange);
    font-weight: 700; font-size: 16px; line-height: 20px; padding: 0 6px;
    color: var(--white);
  }
  .item-list { position: absolute; list-style: none; font-size: 16.5px; line-height: 25px; }
  .item-list li { display: flex; justify-content: space-between; }
  .rule { position: absolute; height: 2px; background: var(--white); }

  .burgers-body { position: absolute; left: 22px; top: 354px; width: 274px; }
  .burgers-body .section-label { position: static; display: inline-block; margin-left: -2px; }
  .burgers-body .item-list { position: static; width: 266px; margin-top: 3px; }
  .burgers-body .item-list li { align-items: flex-start; }
  .burgers-body .item-list .item-name { flex: 1; padding-right: 10px; }
  .burgers-body .rule { position: static; width: 266px; margin: 8px 0 10px; }
  .toppings { font-size: 14.5px; line-height: 22px; }

  .dogs .section-label { left: 14px; top: 26px; }
  .dogs .item-list { left: 22px; top: 48px; width: 262px; }
  .dogs .rule { left: 22px; top: 206px; width: 266px; }
  .dogs-note { position: absolute; left: 0; top: 222px; width: 318px; text-align: center; font-weight: 700; font-size: 16px; }

  .other .section-label { left: 22px; top: 21px; }
  .other .item-list { left: 22px; top: 44px; width: 262px; }

  .food-menu-title {
    position: absolute; left: 26px; top: 380px;
    transform: rotate(-90deg); transform-origin: left top;
    font-size: 17px; letter-spacing: 14px; line-height: 20px;
  }
  .cutlery-illustration {
    position: absolute; left: 58px; top: 54px; width: 156px; height: 348px;
    border-radius: 40px; background: rgba(255,255,255,0.18);
  }

  .wine-illustration {
    position: absolute; left: 768px; top: 768px; width: 78px; height: 144px;
    border-radius: 8px; background: linear-gradient(180deg, rgba(163,36,90,0.55), rgba(163,36,90,0.95));
  }
  .drinks { position: absolute; left: 706px; top: 898px; width: 160px; font-weight: 700; font-size: 16px; line-height: 25px; }
  .drinks-title { font-size: 16px; }
  .drinks ul { list-style: none; }
  .drinks li { display: flex; justify-content: space-between; }

  .sides-list { position: absolute; left: 12px; top: 6px; list-style: none; font-size: 16.4px; line-height: 25px; white-space: nowrap; }
  .sides-list strong { font-weight: 700; }
</style>
</head>
<body>
<main class="menu">
  <div class="woodgrain" role="img" aria-label="Dark woodgrain background"></div>
  <div class="top-swirl-decoration" role="img" aria-label="Red hand-drawn swirl and star decoration"></div>
  <div class="swirl-decoration" role="img" aria-label="Orange hand-drawn scribble circles and star decoration"></div>

  <section class="panel panel--brand burgers">
    <div class="brand-mark"></div>
    <h1 class="brand-name">Juniper's<br>Burgers &amp; Dogs</h1>
    <div class="burgers-body">
      <h2 class="section-label">Burgers</h2>
      <ul class="item-list">
        <li><span class="item-name">Snack Burger</span><span>$3.49</span></li>
        <li><span class="item-name">Snack Cheeseburger</span><span>$3.99</span></li>
        <li><span class="item-name">Juniper's signature Burger</span><span>$4.99</span></li>
        <li><span class="item-name">Juniper's signature Cheeseburger</span><span>$5.49</span></li>
      </ul>
      <div class="rule"></div>
      <p class="toppings">Burger toppings: bacon, lettuce,<br>tomato, onion, pickle, grilled onions,<br>grilled mushrooms,<br>grilled green peppers,<br>jalapeño peppers.</p>
    </div>
  </section>

  <section class="panel panel--dogs dogs">
    <h2 class="section-label">Dogs</h2>
    <ul class="item-list">
      <li><span>Hot Dog</span><span>$2.99</span></li>
      <li><span>Bacon Cheese Hot Dog</span><span>$3.99</span></li>
      <li><span>Slaw Dog</span><span>$3.99</span></li>
      <li><span>Kraut Dog</span><span>$3.49</span></li>
      <li><span>Chili Dog</span><span>$3.99</span></li>
      <li><span>with or with out cheese.</span><span></span></li>
    </ul>
    <div class="rule"></div>
    <p class="dogs-note">Hot dogs are 100% beef</p>
  </section>

  <aside class="panel--food-menu">
    <p class="food-menu-title">FOOD MENU</p>
    <div class="cutlery-illustration" role="img" aria-label="Hand-drawn spoon, knife, plate and fork illustration"></div>
  </aside>

  <section class="panel panel--other other">
    <h2 class="section-label">Other</h2>
    <ul class="item-list">
      <li><span>Grilled Chicken Sandwich</span><span>$5.99</span></li>
      <li><span>Grilled Chicken Sandwich</span><span></span></li>
      <li><span>with cheese</span><span>$6.49</span></li>
      <li><span>(Same toppings as burgers)</span><span></span></li>
    </ul>
  </section>

  <div class="wine-illustration" role="img" aria-label="Wine bottle and glass illustration with stars"></div>
  <section class="drinks">
    <h2 class="drinks-title">Drinks</h2>
    <ul>
      <li><span>32oz. Drink</span><span>$1.88</span></li>
      <li><span>20oz. Drink</span><span>$1.69</span></li>
    </ul>
  </section>

  <section class="panel panel--sides">
    <ul class="sides-list">
      <li>French Fries <strong>$1.99</strong></li>
      <li>Loaded Potatos</li>
      <li>The Plain Tater: <strong>$4.99</strong> choose from: butter, sour cream, cheese, chives</li>
      <li>The Garden Tater: <strong>$5.99</strong> choose from: the Basic plus, broccoli &amp; cheese, grilled mushrooms, onions, &amp; peppers</li>
      <li>The Rancher Tater: <strong>$6.99</strong> choose from the Basic/Veggie plus: grilled chicken, chili, Philly cheesesteak, pulled pork.</li>
    </ul>
  </section>
</main>
</body>
</html>
```